Elmrow Management real estate management company needs presentation folder to hand clients

looking for a folder with pockets that represent my real estate management company when i hand to client reports or promotional material. I only do resedential real estate. I want classy and professional - pictures or additioal graphixs are fine

when a client open i will usally insert text and reports about my business
also on the inside flap is usally place for my business card i will upload a picture so the theme can be constant

Target Market(s)

my existing real estate cleints
and i will use when i am soliciting new business

Industry/Entity Type

Real Estate

Font styles to use
Serif

Requirements
Must have
• must have logo
• must give appearance of professionalism and maturity
• have basic company info tel# ,address
• id like viewer to know I manage real estate - focus on residential small to large apartment buildings
• not strip malls, not giganic complexes - im a mid size company
• logo is black but i welcome color as u see fit
Nice to have
• maybe pictures
• my slogan - " we will manage your building like its our own "
• focus on professioanl, safe, trust worthy
• type style should be clear and readable - but im open to sugestions

```html
<!DOCTYPE html>
<html lang="en">
<head>
<meta charset="utf-8">
<title>Elmrow Management – Presentation Folder</title>
<link rel="stylesheet" href="https://fonts.googleapis.com/css2?family=Roboto:wght@300;400;700&display=swap">
<style>
  :root {
    --bg: #ffffff;
    --folder: #1b1b1b;
    --folder-pocket: #222222;
    --folder-edge: #2c2c2c;
    --emboss: #2e2e2e;
    --paper: #ffffff;
    --ink: #1a1a1a;
    --ink-soft: #555555;
    --brand-grey: #9b9b9b;
    --accent-red: #d94848;
    --white: #ffffff;
  }
  * { box-sizing: border-box; margin: 0; padding: 0; }
  html, body { width: 1200px; height: 1000px; overflow: hidden; background: var(--bg); }
  body { position: relative; font-family: "Roboto", Arial, sans-serif; color: var(--ink); }

  .brand-mark {
    position: absolute; left: 105px; top: 70px;
    display: flex; align-items: center; gap: 12px;
    font-weight: 700; font-size: 30px; color: var(--brand-grey); letter-spacing: 1px;
    text-transform: uppercase;
  }
  .brand-mark .square { width: 26px; height: 26px; background: var(--brand-grey); }

  /* Front cover */
  .cover {
    position: absolute; left: 40px; top: 330px; width: 360px; height: 540px;
    background: var(--folder); border-radius: 0 12px 12px 0;
  }
  .cover .slogan {
    position: absolute; left: 200px; top: 275px;
    color: var(--white); font-weight: 300; font-size: 12.5px; line-height: 16px;
    text-transform: uppercase; letter-spacing: .3px;
  }
  .cover .slogan mark {
    background: var(--white); color: var(--folder); font-weight: 700; padding: 0 3px;
  }
  .cover .emboss-name, .pocket .emboss-name {
    position: absolute; font-weight: 700; color: var(--emboss);
    text-transform: uppercase; letter-spacing: 1px; text-align: center;
  }
  .cover .emboss-name { left: 200px; top: 450px; width: 140px; font-size: 15px; line-height: 18px; }

  /* Inside spread */
  .spread {
    position: absolute; left: 430px; top: 330px; width: 560px; height: 540px;
  }
  .spread .flap-left, .spread .flap-right {
    position: absolute; top: 0; width: 280px; height: 540px; background: var(--folder);
  }
  .spread .flap-left { left: 0; border-right: 1px solid var(--folder-edge); }
  .spread .flap-right { left: 280px; }

  .letterhead {
    position: absolute; left: 300px; top: 20px; width: 240px; height: 420px;
    background: var(--paper); padding: 16px 16px; font-size: 5.6px; line-height: 7.4px; color: var(--ink-soft);
  }
  .letterhead .head { display: flex; justify-content: space-between; margin-bottom: 12px; }
  .letterhead .logo-name { display: flex; align-items: center; gap: 4px; font-weight: 700; font-size: 7px; color: var(--ink); text-transform: uppercase; }
  .letterhead .logo-name .square { width: 8px; height: 8px; background: var(--ink); }
  .letterhead .contact { text-align: right; }
  .letterhead .contact .person { font-weight: 700; font-size: 9px; line-height: 10px; color: var(--ink); }
  .letterhead .contact .role { font-size: 4.5px; text-transform: uppercase; margin-bottom: 3px; }
  .letterhead .contact p { font-size: 4.5px; line-height: 5.5px; }
  .letterhead .body p { margin-bottom: 8px; }
  .letterhead .rule { position: absolute; left: 16px; top: 388px; width: 120px; height: 1px; background: var(--accent-red); }

  .pocket {
    position: absolute; left: 280px; top: 300px; width: 280px; height: 240px;
    background: var(--folder-pocket); border-top: 1px solid var(--folder-edge);
  }
  .pocket .emboss-name { left: 70px; top: 100px; width: 140px; font-size: 15px; line-height: 18px; }

  /* Business card */
  .card {
    position: absolute; left: 1010px; width: 170px; height: 100px; background: var(--folder);
  }
  .card-front { top: 440px; display: flex; align-items: center; justify-content: center; gap: 8px; }
  .card-front .square { width: 12px; height: 12px; background: var(--white); }
  .card-front .name { color: var(--white); font-weight: 700; font-size: 12px; line-height: 14px; text-transform: uppercase; letter-spacing: .5px; }
  .card-back { top: 550px; padding: 6px; }
  .card-back .inner { background: var(--paper); height: 88px; display: flex; padding: 8px 6px; gap: 6px; position: relative; }
  .card-back .logo-name { width: 58px; font-weight: 700; font-size: 7px; line-height: 8px; text-transform: uppercase; color: var(--ink); border-right: 1px solid var(--ink); padding-right: 4px; display: flex; gap: 3px; }
  .card-back .logo-name .square { width: 6px; height: 6px; background: var(--ink); flex: none; }
  .card-back .details .person { font-weight: 700; font-size: 9.5px; color: var(--ink); }
  .card-back .details .role { font-size: 4.5px; text-transform: uppercase; color: var(--ink-soft); margin-bottom: 3px; }
  .card-back .details p { font-size: 4.5px; line-height: 5.5px; color: var(--ink-soft); }
  .card-back .tagline { position: absolute; left: 6px; bottom: 6px; font-size: 4.3px; text-transform: uppercase; color: var(--ink); }
</style>
</head>
<body>

  <div class="brand-mark"><span class="square"></span>Elmrow Management</div>

  <section class="cover">
    <p class="slogan">We will manage<br><mark>Your building</mark> like<br>its our own!</p>
    <p class="emboss-name">Elmrow<br>Management</p>
  </section>

  <section class="spread">
    <div class="flap-left"></div>
    <div class="flap-right"></div>

    <article class="letterhead">
      <div class="head">
        <div class="logo-name"><span class="square"></span>Elmrow Management</div>
        <div class="contact">
          <div class="person">Daniel Hartley</div>
          <div class="role">Master Building Manager</div>
          <p>office: 212-555-0148</p>
          <p>email: daniel@elmrow.com</p>
          <p>cell: 917-555-0173</p>
          <p>48 Linden Ave, Suite 3, Brooklyn NY</p>
        </div>
      </div>
      <div class="body">
        <p>Lorem Ipsum is simply dummy text of the printing and typesetting industry. Lorem Ipsum has been the industry's standard dummy text ever since the 1500s, when an unknown printer took a galley of type and scrambled it to make a type specimen book. It has survived not only five centuries, but also the leap into electronic typesetting, remaining essentially unchanged. It was popularised in the 1960s with the release of Letraset sheets containing Lorem Ipsum passages, and more recently with desktop publishing software including versions of Lorem Ipsum.</p>
        <p>It is a long established fact that a reader will be distracted by the readable content of a page when looking at its layout. The point of using Lorem Ipsum is that it has a more-or-less normal distribution of letters, as opposed to using 'Content here, content here', making it look like readable English. Many desktop publishing packages and web page editors now use Lorem Ipsum as their default model text, and a search for 'lorem ipsum' will uncover many web sites still in their infancy. Various versions have evolved over the years, sometimes by accident, sometimes on purpose.</p>
        <p>Contrary to popular belief, Lorem Ipsum is not simply random text. It has roots in a piece of classical Latin literature from 45 BC, making it over 2000 years old. A Latin professor looked up one of the more obscure Latin words, consectetur, from a Lorem Ipsum passage, and going through the cites of the word in classical literature, discovered the undoubtable source. The generated Lorem Ipsum is therefore always free from repetition or non-characteristic words.</p>
      </div>
      <div class="rule"></div>
    </article>

    <div class="pocket">
      <p class="emboss-name">Elmrow<br>Management</p>
    </div>
  </section>

  <div class="card card-front">
    <span class="square"></span>
    <span class="name">Elmrow<br>Management</span>
  </div>

  <div class="card card-back">
    <div class="inner">
      <div class="logo-name"><span class="square"></span><span>Elmrow Management</span></div>
      <div class="details">
        <div class="person">Daniel Hartley</div>
        <div class="role">Master Building Manager</div>
        <p>office: 212-555-0148</p>
        <p>email: daniel@elmrow.com</p>
        <p>cell: 917-555-0173</p>
        <p>48 Linden Ave, Suite 3, Brooklyn NY</p>
      </div>
      <div class="tagline">We will manage your building like its our own</div>
    </div>
  </div>

</body>
</html>
```